Moroccan Argan Oil label for hair care products

We need a label design for our brand Velmora.
The products are for hair care: Conditoner and Shampoo. We prefer fruit as graphics. The caps of the bottle will be light/apple green, the bottles are white opaque. The label color should be green and/or red/orange. Text on the front side: Moroccan Argan Oil, Shampoo, Strengthens, Hydrates, 474 ml
Please find attached label size.pdf and the bottle. Label size: 50x140 mm.
As the bottles are oval we need one front and one back label.
People in Europe, also african people
Hair

```html
<!DOCTYPE html>
<html lang="en">
<head>
<meta charset="utf-8">
<title>Velmora Organics – Moroccan Argan Oil label font study</title>
<link rel="stylesheet" href="https://fonts.googleapis.com/css2?family=Arimo:wght@400;700&family=Montserrat:wght@400;800&family=Parisienne&family=Cinzel:wght@500&family=Tinos&display=swap">
<style>
  :root {
    --stage: #000000;
    --header-blue: #0c70a6;
    --white: #ffffff;
    --leaf: #5a8a32;
    --leaf-dark: #4a7a28;
    --logo-green: #6a9a36;
    --ink: #222222;
    --mist: #e6f0dc;
    --coconut: #7a4a2a;
    --aloe: #5f9a3c;
  }
  * { box-sizing: border-box; margin: 0; padding: 0; }
  html, body { width: 1200px; height: 1147px; overflow: hidden; background: var(--stage); }
  .sheet { position: relative; width: 1200px; height: 1147px; background: var(--stage); }
  .sheet-header {
    height: 119px; background: var(--header-blue); color: var(--white);
    display: flex; align-items: center; justify-content: center;
    font: 700 46px "Arimo", sans-serif; letter-spacing: 0.5px;
  }
  .variant-number {
    position: absolute; top: 270px; color: var(--white);
    font: 700 44px "Arimo", sans-serif;
  }
  .label {
    position: absolute; top: 400px; width: 220px; height: 616px;
    background: linear-gradient(180deg, var(--white) 0%, var(--white) 62%, var(--mist) 100%);
    overflow: hidden;
  }
  .brand {
    position: absolute; top: 62px; left: 0; right: 0;
    display: flex; align-items: center; justify-content: center; gap: 7px;
    color: var(--logo-green); font: 400 21px "Tinos", serif; line-height: 1.05;
  }
  .brand-square { width: 16px; height: 16px; background: var(--logo-green); flex: none; }
  .brand-name { text-align: left; }
  .product-band {
    position: absolute; top: 196px; left: 10px; right: 10px; height: 70px;
    background: var(--leaf); color: var(--white); text-align: center;
    display: flex; flex-direction: column; justify-content: center;
  }
  .product-name { line-height: 1; }
  .product-name.script { font: 400 34px "Parisienne", cursive; }
  .product-name.bold { font: 800 24px "Montserrat", sans-serif; letter-spacing: 1px; }
  .product-name.regular { font: 400 25px "Arimo", sans-serif; letter-spacing: 1px; }
  .product-sub { font: 400 15px "Arimo", sans-serif; letter-spacing: 1.5px; margin-top: 3px; }
  .hero-art {
    position: absolute; top: 280px; left: 14px; right: 14px; height: 150px;
    background: radial-gradient(ellipse at 62% 50%, var(--coconut) 0%, #a0744f 32%, #dfe9d3 62%, var(--white) 85%);
  }
  .type-band {
    position: absolute; top: 438px; left: 10px; right: 10px; height: 46px;
    background: var(--leaf); color: var(--white);
    display: flex; align-items: center; justify-content: center;
    font: 500 21px "Cinzel", serif; letter-spacing: 2px;
  }
  .benefits {
    position: absolute; top: 496px; left: 0; right: 0; text-align: center;
    color: var(--ink); font: 400 16px "Arimo", sans-serif; line-height: 1.3;
  }
  .aloe-art {
    position: absolute; left: 10px; bottom: 4px; width: 62px; height: 62px;
    background: radial-gradient(ellipse at 50% 80%, var(--aloe) 0%, #8fbf6a 45%, transparent 72%);
  }
  .volume {
    position: absolute; bottom: 14px; left: 0; right: 0; text-align: center;
    color: var(--ink); font: 400 15px "Tinos", serif;
  }
</style>
</head>
<body>
<main class="sheet">
  <header class="sheet-header">CONTRAST: “MOROCCAN font style”</header>

  <span class="variant-number" style="left:80px">1</span>
  <span class="variant-number" style="left:445px">2</span>
  <span class="variant-number" style="left:824px">3</span>

  <section class="label" style="left:134px">
    <div class="brand"><span class="brand-square"></span><span class="brand-name">Velmora<br>Organics</span></div>
    <div class="product-band"><span class="product-name script">Moroccan</span><span class="product-sub">ARGAN OIL</span></div>
    <div class="hero-art" role="img" aria-label="Split coconut with water splash and green leaves"></div>
    <div class="type-band">SHAMPOO</div>
    <p class="benefits">Strengthens<br>Hydrates</p>
    <div class="aloe-art" role="img" aria-label="Aloe vera plant"></div>
    <p class="volume">474 mL</p>
  </section>

  <section class="label" style="left:478px">
    <div class="brand"><span class="brand-square"></span><span class="brand-name">Velmora<br>Organics</span></div>
    <div class="product-band"><span class="product-name bold">MOROCCAN</span><span class="product-sub">ARGAN OIL</span></div>
    <div class="hero-art" role="img" aria-label="Split coconut with water splash and green leaves"></div>
    <div class="type-band">SHAMPOO</div>
    <p class="benefits">Strengthens<br>Hydrates</p>
    <div class="aloe-art" role="img" aria-label="Aloe vera plant"></div>
    <p class="volume">474 mL</p>
  </section>

  <section class="label" style="left:857px">
    <div class="brand"><span class="brand-square"></span><span class="brand-name">Velmora<br>Organics</span></div>
    <div class="product-band"><span class="product-name regular">MOROCCAN</span><span class="product-sub">ARGAN OIL</span></div>
    <div class="hero-art" role="img" aria-label="Split coconut with water splash and green leaves"></div>
    <div class="type-band">SHAMPOO</div>
    <p class="benefits">Strengthens<br>Hydrates</p>
    <div class="aloe-art" role="img" aria-label="Aloe vera plant"></div>
    <p class="volume">474 mL</p>
  </section>
</main>
</body>
</html>
```